Exercise Physiologist needs business cards

I have a logo, I need business cards (Sole trader) as I am moving to a new location and would like an updated look. I provide gym based exercise rehabilitation, injury prevention and movement assessments. I have over 13 years experience as an Exercise Physiologist. I would like the cards to look professional but not boring and can be a little different to stand out when sitting with other Allied Health Professional cards.

Target Market(s)

GP's, Allied health practitioners, people with injuries wanting to exercise

Industry/Entity Type

Health And Wellness

Contact Information for Business Card

Megan Dorrit - Exercise Physiologist 0437 582 906
14 Larkspur Bend Rd
South Harwick
(Gate 5, Brannock Fitness)
vantorahealth@maildrop-example.com
socialpage-example.com/Vantora

Requirements
Must have
• I would like to include a section to add next appointment date and time space to the back of the card.
Nice to have
• Rounded corners and a black background on 1 or 2 sides.
Should not have
• Pictures of fit/toned bodies etc

```html
<!DOCTYPE html>
<html lang="en">
<head>
<meta charset="utf-8">
<title>Vantora Health &amp; Rehabilitation – Business Card</title>
<link href="https://fonts.googleapis.com/css2?family=Arimo:wght@400;700&family=Jura:wght@500;600;700&display=swap" rel="stylesheet">
<style>
  :root {
    --backdrop: #4b4b4d;
    --card-white: #ffffff;
    --brand-blue: #0a5cc4;
    --brand-blue-deep: #0753b6;
    --sky-blue: #5aa6dc;
    --ink: #111111;
    --navy: #2a5a8c;
    --rule: rgba(255,255,255,0.55);
  }
  * { box-sizing: border-box; margin: 0; padding: 0; }
  html, body {
    width: 1200px; height: 1000px; overflow: hidden;
    background: var(--backdrop);
  }
  .stage { position: relative; width: 1200px; height: 1000px; }

  .card {
    position: absolute; left: 250px; width: 700px; height: 400px;
    border-radius: 26px; overflow: hidden;
  }

  /* Appointment side */
  .card--appointment { top: 70px; background: var(--card-white); }
  .brand {
    position: absolute; left: 130px; top: 66px;
    display: flex; align-items: center; gap: 20px;
  }
  .brand__dot {
    width: 116px; height: 116px; border-radius: 50%;
    background: var(--sky-blue);
    flex: none;
  }
  .brand__text { display: flex; flex-direction: column; }
  .brand__name {
    font-family: "Arimo", sans-serif; font-weight: 700;
    font-size: 80px; line-height: 1; color: var(--brand-blue);
  }
  .brand__tagline {
    font-family: "Arimo", sans-serif; font-size: 19px;
    color: var(--navy); letter-spacing: 1px; margin-top: 12px;
  }
  .appointment {
    position: absolute; left: 0; right: 0; top: 262px;
    font-family: "Arimo", sans-serif; color: var(--ink);
  }
  .appointment__title {
    text-align: center; font-weight: 700; font-size: 19px; letter-spacing: 0.5px;
  }
  .appointment__fields {
    display: flex; justify-content: space-between;
    padding: 0 120px; margin-top: 26px; font-size: 15px; font-weight: 700;
  }

  /* Contact side */
  .card--contact { top: 530px; background: var(--brand-blue); }
  .contact__disc {
    position: absolute; right: -50px; top: 80px;
    width: 340px; height: 340px; border-radius: 50%;
    background: var(--brand-blue-deep);
  }
  .contact {
    position: absolute; left: 40px; right: 40px; top: 250px;
    font-family: "Jura", sans-serif; color: #fff;
  }
  .contact__name {
    font-weight: 700; font-size: 24px; color: var(--sky-blue); letter-spacing: 1px;
  }
  .contact__role { font-size: 15px; font-weight: 700; color: #fff; margin-left: 8px; letter-spacing: 0.5px; }
  .contact__line { font-size: 14px; font-weight: 700; margin-top: 7px; letter-spacing: 0.3px; }
  .contact__label { color: var(--sky-blue); }
  .contact__social { margin-left: 34px; }
  .contact__rule { height: 1px; background: var(--rule); margin-top: 12px; }
</style>
</head>
<body>
<main class="stage">
  <section class="card card--appointment">
    <div class="brand">
      <span class="brand__dot"></span>
      <div class="brand__text">
        <span class="brand__name">vantora</span>
        <span class="brand__tagline">HEALTH &amp; REHABILITATION</span>
      </div>
    </div>
    <div class="appointment">
      <p class="appointment__title">NEXT APPOINTMENT</p>
      <div class="appointment__fields">
        <span>DATE.........................</span>
        <span>TIME.........................</span>
      </div>
    </div>
  </section>

  <section class="card card--contact">
    <span class="contact__disc"></span>
    <div class="contact">
      <p><span class="contact__name">MEGAN DORRIT</span><span class="contact__role">EXERCISE PHYSIOLOGIST</span></p>
      <p class="contact__line"><span class="contact__label">A:</span> 14 Larkspur Bend Rd South Harwick (Gate 5, Brannock Fitness) | <span class="contact__label">T:</span> 0437 582 906</p>
      <p class="contact__line"><span class="contact__label">E:</span> vantorahealth@maildrop-example.com<span class="contact__social">socialpage-example.com/Vantora</span></p>
      <div class="contact__rule"></div>
    </div>
  </section>
</main>
</body>
</html>
```